The label Velombri Dijon Mustard

Hello everybody,
What we need : a design for a label of Dijon Mustard it's a new project and. What we're looking for : a european style with a warm vibe. The product's target : the North American.

The design must be elegant, modern and up market.don't hesitate to think outside the box.
we attached a file contain our logo. the logo for this product will be the main logo the third one.
and we attached a sizes and the inspiration design LUVETTE and CORBIN

Target Market(s)

North America

Logo Text

Velombri

Logo styles of interest
Wordmark Logo
Font styles to use
Serif
Script

Colors

Designer to choose colors to be used in the design.

Requirements
Must have
• -The brand ''Velombri'' and the logo is (the Main logo The Third one) attached file.
• - the name of the product, ''Dijon Mustard /Moutarde de Dijon/ ديجون الخردل'', in English, French and Arabic
• -The Lid will be red or black depend of your design.
• - the nutrition fact. Make a place and it will be changed by us.
• -Ingrediants:
• fr: eau, graines de MOUTARDE, vinaigre d'alcool, sel, acidifiant : acide citrique, conservateur : E224 (SULFITES).
• En: water, MUSTARD seeds, alcohol vinegar, salt, acidifier: citric acid, preservative: E224 (SULFITES).
• Ar: ماء ، بذور الخردل ، خل الكحول ، الملح ، محمض: حمض الستريك ، مواد حافظة: E224
• - the weight of 295g/ 250ml
• - conditioned by Sarl Velombri/conditionné par Sarl Velombri.
• -Slogan In French''Apportez le vrai goût à votre maison''
• -design must be elegant, modern and up market.
Nice to have
• -A minimalist design style
• -Design color: red or black.

```html
<!DOCTYPE html>
<html lang="en">
<head>
<meta charset="utf-8">
<title>Velombri Dijon Mustard – Label</title>
<link rel="stylesheet" href="https://fonts.googleapis.com/css2?family=Cormorant+Garamond:wght@400;500;700&family=Pinyon+Script&family=Roboto:wght@400;500&family=Amiri&display=swap">
<style>
  :root {
    --canvas: #ffffff;
    --label: #3c4039;
    --frame: #a9a692;
    --cream: #efe8d6;
    --brand-red: #d62a1e;
    --accent-red: #d9574a;
    --ink-light: #d9d4c4;
    --ink-soft: #a9a797;
    --ink-faint: #5a5f56;
    --script-ink: #4b4c45;
    --caption: #3a3a3a;
  }
  * { box-sizing: border-box; margin: 0; padding: 0; }
  html, body { width: 1200px; height: 1200px; overflow: hidden; background: var(--canvas); }
  .sheet { position: relative; width: 1200px; height: 1200px; }

  .label { position: absolute; }
  .label-shape { position: absolute; inset: 0; }
  .caption {
    position: absolute; width: 100%; top: 100%; margin-top: 34px; text-align: center;
    font-family: "Cormorant Garamond", serif; font-size: 15px; letter-spacing: 3px; color: var(--caption);
  }

  /* Front */
  .label-front { left: 92px; top: 303px; width: 372px; height: 543px; }
  .front-clip { position: absolute; left: 0; top: 42px; width: 372px; height: 501px; overflow: hidden; }
  .brand-name {
    position: absolute; top: 100px; width: 100%; text-align: center;
    font-family: "Cormorant Garamond", serif; font-weight: 700; font-size: 60px;
    letter-spacing: 1px; color: var(--brand-red); line-height: 1;
  }
  .product-band {
    position: absolute; left: -40px; top: 220px; width: 460px; height: 62px;
    background: var(--cream); transform: rotate(-15deg); transform-origin: center;
    display: flex; align-items: center; justify-content: center;
  }
  .product-name-fr {
    font-family: "Pinyon Script", cursive; font-size: 38px; color: var(--script-ink);
    padding-left: 30px;
  }
  .product-name-en {
    position: absolute; top: 348px; width: 100%; text-align: center;
    font-family: "Cormorant Garamond", serif; font-size: 16px; letter-spacing: 3px; color: var(--ink-light);
  }
  .front-rule { position: absolute; top: 376px; left: 81px; width: 210px; height: 1px; background: var(--frame); }
  .product-name-ar {
    position: absolute; top: 384px; width: 100%; text-align: center;
    font-family: "Amiri", serif; font-size: 20px; color: var(--ink-light);
  }
  .front-weight {
    position: absolute; top: 452px; width: 100%; text-align: center;
    font-family: "Cormorant Garamond", serif; font-size: 15px; color: var(--ink-faint); letter-spacing: 1px;
  }

  /* Back */
  .label-back { left: 654px; top: 345px; width: 460px; height: 501px; }
  .back-column { position: absolute; left: 50px; top: 0; width: 190px; height: 100%; }
  .slogan {
    position: absolute; top: 38px; font-family: "Cormorant Garamond", serif; font-weight: 500;
    font-size: 17px; line-height: 1.3; letter-spacing: 2px; color: var(--accent-red); text-transform: uppercase;
  }
  .rule { position: absolute; left: 0; width: 190px; height: 1px; background: var(--frame); }
  .section-title {
    position: absolute; top: 118px; font-family: "Cormorant Garamond", serif; font-size: 14px;
    letter-spacing: 3px; color: var(--ink-soft);
  }
  .ingredients {
    position: absolute; left: 0; width: 190px; font-family: "Cormorant Garamond", serif;
    font-size: 12px; line-height: 1.45; color: var(--ink-soft);
  }
  .ingredients-ar { font-family: "Amiri", serif; font-size: 11.5px; direction: rtl; text-align: left; }
  .packer {
    position: absolute; top: 390px; font-family: "Cormorant Garamond", serif; font-size: 14px;
    line-height: 1.35; color: var(--accent-red);
  }
  .net-weight {
    position: absolute; right: 22px; top: 417px; font-family: "Cormorant Garamond", serif;
    font-size: 14px; color: var(--ink-soft); letter-spacing: 1px;
  }

  .nutrition {
    position: absolute; left: 262px; top: 30px; width: 180px; border: 1.5px solid var(--ink-light);
    padding: 6px 7px; font-family: "Roboto", sans-serif; color: var(--ink-light); font-size: 8.5px; line-height: 1.35;
  }
  .nutrition-title { font-family: "Cormorant Garamond", serif; font-size: 13px; letter-spacing: 2px; padding-bottom: 3px; border-bottom: 1px solid var(--ink-light); }
  .nutrition-row { display: flex; justify-content: space-between; padding: 3px 0; border-bottom: 1px solid var(--ink-light); }
  .nutrition-row.plain { border-bottom: none; padding: 1px 0; }
  .nutrition-row.thick { border-bottom-width: 3px; }
  .nutrition-row.major { font-style: italic; font-size: 9.5px; }
  .nutrition-row.indent { padding-left: 10px; }
  .nutrition-row.indent2 { padding-left: 20px; }
  .nutrition-row .dv { font-style: normal; }
  .calories { font-size: 11px; }
  .dv-head { justify-content: flex-end; font-size: 7.5px; }
</style>
</head>
<body>
<main class="sheet">

  <section class="label label-front" aria-label="Front label">
    <svg class="label-shape" width="372" height="543" viewBox="0 0 372 543" aria-hidden="true">
      <path fill="var(--label)" d="M0,42 H44 Q62,42 62,24 Q62,0 86,0 H286 Q310,0 310,24 Q310,42 328,42 H372 V543 H0 Z"/>
      <path fill="none" stroke="var(--frame)" stroke-width="1"
        d="M22,56 H52 Q74,56 74,34 Q74,14 94,14 H278 Q298,14 298,34 Q298,56 320,56 H350
           A8,8 0 0 0 358,64 V521 A8,8 0 0 0 350,529 H22 A8,8 0 0 0 14,521 V64 A8,8 0 0 0 22,56 Z"/>
    </svg>
    <div class="front-clip">
      <div class="brand-name">Velombri</div>
      <div class="product-band"><span class="product-name-fr">Moutarde de Dijon</span></div>
      <div class="product-name-en">DIJON MUSTARD</div>
      <div class="front-rule"></div>
      <div class="product-name-ar" lang="ar" dir="rtl">ديجون الخردل</div>
      <div class="front-weight">295g / 250ml</div>
    </div>
    <div class="caption">FRONT</div>
  </section>

  <section class="label label-back" aria-label="Back label">
    <svg class="label-shape" width="460" height="501" viewBox="0 0 460 501" aria-hidden="true">
      <rect width="460" height="501" fill="var(--label)"/>
      <path fill="none" stroke="var(--frame)" stroke-width="1"
        d="M22,14 H438 A8,8 0 0 0 446,22 V479 A8,8 0 0 0 438,487 H22 A8,8 0 0 0 14,479 V22 A8,8 0 0 0 22,14 Z"/>
    </svg>

    <div class="back-column">
      <p class="slogan">Apportez le<br>vrai goût<br>à votre maison</p>
      <div class="rule" style="top:104px"></div>
      <h2 class="section-title">INGREDIENTS</h2>
      <div class="rule" style="top:144px"></div>
      <p class="ingredients" style="top:160px">Fr: Eau, Graines De Moutarde, Vinaigre D'alcool, Sel, Acidifiant : Acide Citrique, Conservateur : E224 (Sulfites).</p>
      <div class="rule" style="top:228px"></div>
      <p class="ingredients" style="top:242px">En: Water, Mustard Seeds, Alcohol Vinegar, Salt, Acidifier: Citric Acid, Preservative: E224 (Sulfites).</p>
      <div class="rule" style="top:310px"></div>
      <p class="ingredients ingredients-ar" style="top:322px" lang="ar">Ar: ماء ، بذور الخردل ، خل الكحول ، الملح ، محمض: حمض الستريك ، مواد حافظة: E224</p>
      <div class="rule" style="top:380px"></div>
      <p class="packer">Conditioned by Sarl Velombri/<br>conditionné par Sarl Velombri</p>
    </div>

    <div class="nutrition" aria-label="Nutrition facts">
      <div class="nutrition-title">NUTRITION FACTS</div>
      <div class="nutrition-row plain">10 servings per container</div>
      <div class="nutrition-row thick">Serving size 1 tea stick (1.2gr)</div>
      <div class="nutrition-row plain">Amount per Serving</div>
      <div class="nutrition-row thick calories"><span>Calories</span><span>0</span></div>
      <div class="nutrition-row dv-head"><span>% Daily Value*</span></div>
      <div class="nutrition-row major"><span>Total Fat 0g</span><span class="dv">0%</span></div>
      <div class="nutrition-row indent"><span>Saturated Fat 0g</span><span>0%</span></div>
      <div class="nutrition-row indent"><span>Trans Fat 0g</span><span></span></div>
      <div class="nutrition-row major"><span>Cholestrol 0mg</span><span class="dv">0%</span></div>
      <div class="nutrition-row major"><span>Sodium 0g</span><span class="dv">0%</span></div>
      <div class="nutrition-row major"><span>Total Carbohydrate 0g</span><span class="dv">0%</span></div>
      <div class="nutrition-row indent"><span>Dietary Fiber 0g</span><span>0%</span></div>
      <div class="nutrition-row indent"><span>Total Sugars 0g</span><span></span></div>
      <div class="nutrition-row indent2 plain"><span>Includes 0g Added Sugars</span><span>0%</span></div>
    </div>

    <div class="net-weight">295g/ 250ml</div>
    <div class="caption">BACK</div>
  </section>

</main>
</body>
</html>
```